High end landscaping & service company needs brochure design

Please check out our website.

We would like the brochure to be about our landscape Construction (Outdoor Kitchens, water features, gardens), Turf Care (Fertilizer, aeration, over seeding), property maintenance (Lawn maintenance, Gardens)

I would like our brochure to have a similar theme and look as our current post card and website. Our website is www.halvernbrookyards.com

Please let me know if you need any further information. dorell@halvernbrookyards.com

Thanks,

Target Market(s)

High End commercial and residential clients

Industry/Entity Type

Property Maintenance

Requirements
Must have
• BRIEF price list for Turf Care

Use contact info on website.

1 double sided page so we can print it and mail it OR send it as a email.

```html
<!DOCTYPE html>
<html lang="en">
<head>
<meta charset="utf-8">
<title>2014 Turf Care Package Price Options</title>
<link href="https://fonts.googleapis.com/css2?family=Oswald:wght@500;700&family=Open+Sans:wght@400;600;700&family=PT+Sans+Narrow:wght@400;700&display=swap" rel="stylesheet">
<style>
:root{
  --ink:#333333;
  --paper:#ffffff;
  --panel-light:#9fd14e;
  --panel-dark:#7cb82f;
  --panel-edge:#2b2b2b;
  --tier-dark:#141414;
  --tier-mid:#3a3a3a;
  --cost-light:#3db54a;
  --cost-dark:#0a7a3a;
  --save-light:#2f7fd0;
  --save-dark:#1a3f8f;
  --bar-light:#ffffff;
  --bar-shade:#d8d8d8;
  --brand-green:#1f8a3a;
  --brand-grey:#4a4a4a;
}
*{margin:0;padding:0;box-sizing:border-box}
html,body{width:940px;height:1200px;overflow:hidden;background:var(--paper)}
.sheet{position:relative;width:940px;height:1200px;background:linear-gradient(#ffffff,#f3f3f3);font-family:"Open Sans",sans-serif;color:var(--ink)}
.headline{position:absolute;left:64px;top:64px;width:808px;text-align:center;font-family:"Oswald",sans-serif;font-weight:700;font-size:45px;letter-spacing:.3px;color:var(--ink);line-height:1;white-space:nowrap}
.price-panel{position:absolute;left:67px;top:137px;width:805px;height:527px;border-radius:20px;border:3px solid var(--panel-edge);background:linear-gradient(180deg,var(--panel-light),var(--panel-dark));box-shadow:0 4px 6px rgba(0,0,0,.3)}
.panel-title{position:absolute;left:26px;top:10px;font-family:"Oswald",sans-serif;font-weight:700;font-size:37px;color:#fff;text-shadow:2px 2px 2px rgba(0,0,0,.55);letter-spacing:.5px}
.panel-rule{position:absolute;left:14px;right:14px;top:67px;height:1px;background:rgba(255,255,255,.7)}
.tier{position:absolute;left:12px;width:785px}
.tier-name{position:absolute;left:0;top:6px;width:122px;height:40px;border-radius:20px;background:linear-gradient(var(--tier-mid),var(--tier-dark));color:#fff;font-family:"PT Sans Narrow",sans-serif;font-weight:700;font-size:21px;display:flex;align-items:center;justify-content:center;border:2px solid #fff;letter-spacing:.5px}
.tier-detail{position:absolute;left:115px;top:0;width:400px;height:52px;border-radius:0 26px 26px 0;background:linear-gradient(var(--bar-light),var(--bar-shade));border-left:6px solid var(--brand-green);padding:7px 0 0 22px;font-size:12.5px;line-height:18px;color:#222;white-space:nowrap}
.tier-cost{position:absolute;left:523px;top:3px;width:106px;height:46px;border-radius:23px;background:linear-gradient(var(--cost-light),var(--cost-dark));color:#fff;font-family:"PT Sans Narrow",sans-serif;font-size:20px;display:flex;align-items:center;justify-content:center;border:2px solid #fff;white-space:nowrap}
.tier-save{position:absolute;left:633px;top:3px;width:152px;height:46px;border-radius:23px;background:linear-gradient(var(--save-light),var(--save-dark));color:#fff;font-family:"PT Sans Narrow",sans-serif;font-size:20px;display:flex;align-items:center;justify-content:center;border:2px solid #fff;white-space:nowrap}
.tier-bronze{top:84px}
.tier-silver{top:157px}
.tier-gold{top:229px}
.tier-platinum{top:303px}
.tier-platinum .tier-detail{height:66px;top:-7px;padding-top:6px}
.tier-platinum .tier-name{top:6px}
.rate{position:absolute;font-size:12.5px;color:#222;white-space:nowrap}
.rate h3{font-weight:700;font-size:15.5px;letter-spacing:.2px;margin-bottom:4px;color:#1a1a1a}
.rate b{font-weight:700}
.rate .gap{display:inline-block;width:26px}
.rate-weed{left:30px;top:392px}
.rate-overseed{left:374px;top:392px}
.rate-fertilizer{left:30px;top:455px}
.rate-injection{left:374px;top:455px;line-height:19px}
.rate-rule-v{position:absolute;left:357px;top:388px;width:1px;height:130px;background:rgba(255,255,255,.7)}
.rate-rule-h{position:absolute;left:14px;right:14px;top:445px;height:1px;background:rgba(255,255,255,.7)}
.photo{position:absolute;top:696px;height:321px;border-radius:40px;border:3px solid #555;box-shadow:0 3px 6px rgba(0,0,0,.35)}
.photo-home{left:67px;width:528px;background:linear-gradient(180deg,#c9d8e6 0%,#e6e1d3 35%,#b8a98e 55%,#4f7a2f 75%,#3f6b25 100%)}
.photo-garden{left:615px;width:257px;background:linear-gradient(180deg,#6f9a3a 0%,#98b858 45%,#d86a4a 68%,#e9c36a 80%,#4f8a2a 100%)}
.brand{position:absolute;left:82px;top:1060px;display:flex;align-items:center;gap:14px}
.brand-dot{width:52px;height:52px;border-radius:50%;background:var(--brand-green)}
.brand-name{font-family:"Open Sans",sans-serif;font-weight:600;font-size:22px;line-height:27px;color:var(--brand-grey);letter-spacing:1.5px}
.contact{position:absolute;left:410px;top:1044px;width:460px;text-align:center}
.contact-line{font-family:"Oswald",sans-serif;font-weight:700;color:var(--ink);white-space:nowrap;line-height:52px}
.contact-line .label{font-size:29px}
.contact-line .phone{font-size:41px;margin-left:6px}
.contact-note{margin-top:6px;font-size:12px;line-height:21px;color:#333;white-space:nowrap}
</style>
</head>
<body>
<main class="sheet">
  <h1 class="headline">2014 TURF CARE PACKAGE PRICE OPTIONS</h1>

  <section class="price-panel">
    <h2 class="panel-title">Based on 3000sq ft</h2>
    <div class="panel-rule"></div>

    <div class="tier tier-bronze">
      <div class="tier-detail">3x Timely applications of Premium grade Fertilizer<br>1x Weed Spray application</div>
      <div class="tier-name">BRONZE</div>
      <div class="tier-cost">Cost $299.99</div>
      <div class="tier-save">$109.99 Savings</div>
    </div>
    <div class="tier tier-silver">
      <div class="tier-detail">Fertilize 4x annually,&nbsp;&nbsp; 2x Weed spray application<br>1x chinch bug prevention</div>
      <div class="tier-name">SILVER</div>
      <div class="tier-cost">Cost $469.99</div>
      <div class="tier-save">$259.96 Savings</div>
    </div>
    <div class="tier tier-gold">
      <div class="tier-detail">Spring Aeration,&nbsp;&nbsp;&nbsp; Fertilize 4x annually<br>2x weed spray application,&nbsp; 1x chinch bug prevention</div>
      <div class="tier-name">GOLD</div>
      <div class="tier-cost">Cost $499.99</div>
      <div class="tier-save">$259.96 Savings</div>
    </div>
    <div class="tier tier-platinum">
      <div class="tier-detail">Spring Aeration , Over seed with "Renew &amp; Root" ($200 Value),<br>Fertilize 4x annually,&nbsp; 3x weed spray application<br>1x chinch bug prevention,&nbsp;&nbsp; Fall aeration</div>
      <div class="tier-name">PLATINUM</div>
      <div class="tier-cost">Cost $799.99</div>
      <div class="tier-save">$274.96 Savings</div>
    </div>

    <div class="rate-rule-v"></div>
    <div class="rate-rule-h"></div>

    <div class="rate rate-weed">
      <h3>WEED SPRAY APPLICATION</h3>
      <p>Cost $139.99/application<span class="gap"></span><b>($24/1000sqft after)</b></p>
    </div>
    <div class="rate rate-overseed">
      <h3>RENEW &amp; ROOT OVERSEED</h3>
      <p>Cost 199.99/Applied<span class="gap"></span><span class="gap"></span><span class="gap"></span><b>(27/1000sqft after)</b></p>
    </div>
    <div class="rate rate-fertilizer">
      <h3>FERTILIZER APPLICATION</h3>
      <p>Cost $89.99/application<span class="gap"></span><b>($6/1000sqft after)</b></p>
    </div>
    <div class="rate rate-injection">
      <h3>DEEP ROOT INJECTION</h3>
      <p>$10/Tree/Application,&nbsp;&nbsp; 1 tree = 8 injections,&nbsp;&nbsp; Minimum $60 Charge<br>Recommended 2x seasonally ,&nbsp; 8.5/Tree/Application After 10 tree's</p>
    </div>
  </section>

  <div class="photo photo-home" role="img" aria-label="Photo of a large stone-front home with a landscaped lawn and garden beds"></div>
  <div class="photo photo-garden" role="img" aria-label="Photo of colourful flower beds and trees being watered by a sprinkler"></div>

  <div class="brand">
    <span class="brand-dot"></span>
    <span class="brand-name">HALVERNBROOK<br>YARDS GROUP</span>
  </div>

  <div class="contact">
    <p class="contact-line"><span class="label">Contact us:</span><span class="phone">519-555-0187</span></p>
    <p class="contact-note">With 20+ years of experience, and a focus on quality and organization we<br>are your #1 choice when it comes to all things landscaping.</p>
  </div>
</main>
</body>
</html>
```